Etiketten-Design für Weinflaschen gesucht
Zielgruppe
Wir sind ein Weingut und suchen für unsere Weinflaschen ein neues Etikettdesign.
Aufgabenstellung
Im Anhang sieht man unsere leeren Weinflaschen mit den neuen Kapseln. Dazu passend suchen wir die Etiketten.
Grundfarbe des Etikettes ist Weiß, Größe ca. 11cm hoch & 9cm breit!
Jede Sorte hat ihrer eigene Farbe - diese ist am Kapsel sichtbar und soll sich auch leicht im Etikett
wieder finden.
Etiketten vom Grunddesign gleich + jedoch nur an STELLEN ANDERS EINGEFÄRBT.
Am Etikett zu finden sollte sein:
- Unser Logo mit Namen (Weingut muss nicht vorhanden sein am Etikett)
- Kirchenlogo
- Sorte von Wein:
(Grüner Veltliner - Grün
Traminer - Blau
Rheinriesling - Orange
Blaufränkisch - Rot
St.Lauerent -Gelb
Zweigelt - Weiß)

```html
<!DOCTYPE html>
<html lang="de">
<head>
<meta charset="utf-8">
<title>Lindgruber – Etiketten Rotwein</title>
<link rel="stylesheet" href="https://fonts.googleapis.com/css2?family=Montserrat:wght@300;400&display=swap">
<style>
  :root {
    --backdrop: #c89d67;
    --label-white: #ffffff;
    --ink: #111111;
    --gold: #d9b45f;
    --gold-light: #e8cf8f;
    --blaufraenkisch: #d9284b;
    --st-laurent: #f2c81c;
    --zweigelt: #ffffff;
    --sketch-dark: #5b5b5b;
    --sketch-light: #d6d6d6;
  }
  * { box-sizing: border-box; margin: 0; padding: 0; }
  html, body {
    width: 1200px;
    height: 848px;
    overflow: hidden;
    background: var(--backdrop);
    font-family: "Montserrat", sans-serif;
  }
  .label-row {
    width: 1200px;
    height: 848px;
    display: flex;
    justify-content: center;
    align-items: center;
    gap: 90px;
  }
  .wine-label {
    position: relative;
    width: 270px;
    height: 330px;
    background: var(--label-white);
    overflow: hidden;
    box-shadow: 0 2px 8px rgba(0,0,0,0.12);
  }
  .label-bands {
    position: absolute;
    inset: 0;
    width: 100%;
    height: 100%;
  }
  .brand-dot {
    position: absolute;
    top: 26px;
    left: 50%;
    width: 38px;
    height: 38px;
    margin-left: -19px;
    border-radius: 50%;
    background: var(--ink);
  }
  .brand-name {
    position: absolute;
    top: 76px;
    left: 0;
    width: 100%;
    text-align: center;
    font-weight: 400;
    font-size: 26px;
    letter-spacing: 0.5px;
    color: var(--ink);
  }
  .variety-name {
    position: absolute;
    top: 172px;
    left: 28px;
    font-weight: 300;
    font-size: 12px;
    letter-spacing: 0.3px;
    color: var(--ink);
    text-transform: uppercase;
  }
  .church-sketch {
    position: absolute;
    right: 12px;
    bottom: 14px;
    width: 90px;
    height: 82px;
    background: radial-gradient(ellipse at 50% 60%, var(--sketch-dark) 0%, var(--sketch-light) 70%, transparent 100%);
    opacity: 0.8;
  }
</style>
</head>
<body>
<main class="label-row">

  <article class="wine-label label--blaufraenkisch">
    <svg class="label-bands" viewBox="0 0 270 330" aria-hidden="true">
      <polygon points="66,330 100,330 270,105 270,60" fill="var(--blaufraenkisch)"/>
      <line x1="60" y1="330" x2="270" y2="52" stroke="var(--gold)" stroke-width="2"/>
      <line x1="106" y1="330" x2="270" y2="113" stroke="var(--gold)" stroke-width="2"/>
      <circle cx="198" cy="185" r="9" fill="none" stroke="var(--label-white)" stroke-width="2"/>
    </svg>
    <div class="brand-dot"></div>
    <p class="brand-name">Lindgruber</p>
    <p class="variety-name">Blaufränkisch</p>
    <div class="church-sketch" role="img" aria-label="Federzeichnung der Dorfkirche auf dem Hügel"></div>
  </article>

  <article class="wine-label label--st-laurent">
    <svg class="label-bands" viewBox="0 0 270 330" aria-hidden="true">
      <polygon points="66,330 100,330 270,105 270,60" fill="var(--st-laurent)"/>
      <line x1="60" y1="330" x2="270" y2="52" stroke="var(--gold)" stroke-width="2"/>
      <line x1="106" y1="330" x2="270" y2="113" stroke="var(--gold)" stroke-width="2"/>
      <circle cx="198" cy="185" r="9" fill="none" stroke="var(--label-white)" stroke-width="2"/>
    </svg>
    <div class="brand-dot"></div>
    <p class="brand-name">Lindgruber</p>
    <p class="variety-name">St.Lauerent</p>
    <div class="church-sketch" role="img" aria-label="Federzeichnung der Dorfkirche auf dem Hügel"></div>
  </article>

  <article class="wine-label label--zweigelt">
    <svg class="label-bands" viewBox="0 0 270 330" aria-hidden="true">
      <line x1="52" y1="330" x2="270" y2="40" stroke="var(--gold-light)" stroke-width="2.5"/>
      <line x1="100" y1="330" x2="270" y2="104" stroke="var(--gold-light)" stroke-width="2.5"/>
      <circle cx="190" cy="172" r="9" fill="var(--ink)"/>
    </svg>
    <div class="brand-dot"></div>
    <p class="brand-name">Lindgruber</p>
    <p class="variety-name" style="top:166px;left:70px;">Zweigelt</p>
    <div class="church-sketch" role="img" aria-label="Federzeichnung der Dorfkirche auf dem Hügel"></div>
  </article>

</main>
</body>
</html>
```